Sacred Anointing Oils need new label

Beautiful sacred oils need a new label. There are 4 oils with 4 key colours. The labels need to match together, so they look good on a shop shelf. They have a feeling of warmth, simplicity, beauty, non religious, yet sacred. Engaging. I have now created a photoshop mockup of what I like and will attach the psd files.
I will attach the current cards to give you more of a feel of the oils. There is not a card yet for Halbrey. The cards will also need to be changed, as another project, once the labels are completed.

There are 4 Oils, Spikenard, Verolinde, Halbrey, Amber Hush. They each have matching cards to go with them. The labels go on 15ml cobalt blue glass bottles. The size is 85mm x 42mm including bleed. I need them laid out on an A4 sheet, I can fit 12 per page. Slightly rounded corners. Each bottle is the same layout, different colour scheme. Header font is Apple chancery.

Target Market(s)

Women 15-80

Industry/Entity Type

Shop

Contact Information for Business Card

Please see attached information and logo

Font styles to use
Other font styles liked:
• There will be simple san serif font for the contents details. the title name eg Verolinde can be more script or decorative. I have used QumpellikaNo12 in the past, and Apple Chancery. am open to similar options.

Requirements
Must have
• 4 labels are attached with the mockup design of what I want. Must be
• clear and easy to read, a feeling of warmth, rich colours. Must be one label per bottle (not two), rectangular wrapping around bottle. Not 2 labels per bottle. The label size must be 42mm height and a minimum of 88mm in length around bottle - this includes bleed. The actual height of the label, without bleed must be a maximum of 37mm and width 89mm max.
Nice to have
• The image from logo needs to be eye catching and drawing people in, a sense of flow.
Should not have
• Must not be clunky, hard to read, two labels. No religious imagery

```html
<!DOCTYPE html>
<html lang="en">
<head>
<meta charset="utf-8">
<title>Lumen Vessel – Oil of Anointing Labels</title>
<link rel="stylesheet" href="https://fonts.googleapis.com/css2?family=Playball&family=Open+Sans:wght@400;600&family=Josefin+Sans:wght@400&display=swap">
<style>
  :root {
    --page: #ffffff;
    --ink-light: #ffffff;
    --ink-brand: #6a1a22;
    --ink-dark: #1a1a1a;
    --mark: #a3195b;
    --silver: linear-gradient(90deg, #8f8f8f, #f2f2f2 30%, #b3b3b3 55%, #f7f7f7 80%, #9a9a9a);
    --gold: linear-gradient(90deg, #a8801f, #f3d37a 30%, #c59a2e 55%, #f8e29a 80%, #a8801f);
    --verolinde: linear-gradient(180deg, #a12a22, #912019);
    --spikenard: #151a33;
    --amber-hush: linear-gradient(180deg, #e5592a, #dc3a2b);
    --halbrey: #eeaa92;
  }
  * { box-sizing: border-box; margin: 0; padding: 0; }
  html, body { width: 1200px; height: 621px; overflow: hidden; background: var(--page); }
  .sheet { position: relative; width: 1200px; height: 621px; }

  .label {
    position: absolute; width: 556px; height: 253px;
    border-radius: 7px; overflow: hidden; color: var(--ink-light);
    font-family: "Open Sans", Arial, sans-serif;
  }
  .label::before, .label::after {
    content: ""; position: absolute; left: 0; right: 0; height: 6px;
    background: var(--trim);
  }
  .label::before { top: 0; }
  .label::after { bottom: 0; }

  .label--verolinde { left: 24px; top: 41px; background: var(--verolinde); --trim: var(--silver); }
  .label--spikenard { left: 620px; top: 41px; background: var(--spikenard); --trim: var(--gold); }
  .label--amber-hush { left: 24px; top: 325px; background: var(--amber-hush); --trim: var(--silver); }
  .label--halbrey { left: 620px; top: 325px; background: var(--halbrey); --trim: var(--gold); }
  .label--halbrey .details { font-weight: 600; }

  .details {
    position: absolute; left: 25px; top: 16px; width: 180px;
    font-size: 10.5px; line-height: 1.32;
  }
  .details .heading { margin-bottom: 12px; }
  .details .contact { position: absolute; top: 133px; left: 0; width: 180px; }

  .title {
    position: absolute; left: 214px; width: 207px; top: 8px; text-align: center;
    font-family: "Playball", "Brush Script MT", cursive;
    font-size: 38px; line-height: 1.2; white-space: nowrap;
  }
  .subtitle {
    position: absolute; left: 194px; width: 247px; top: 59px; text-align: center;
    font-family: "Josefin Sans", Arial, sans-serif; font-size: 13px; letter-spacing: 1.3px;
  }

  .arch {
    position: absolute; left: 214px; top: 98px; width: 207px; height: 160px;
    border-radius: 104px 104px 0 0; background: var(--trim);
  }
  .arch__inner {
    position: absolute; left: 7px; right: 7px; top: 7px; bottom: 0;
    border-radius: 97px 97px 0 0; background: #ffffff;
    display: flex; flex-direction: column; align-items: center;
  }
  .brand-dot {
    width: 36px; height: 36px; border-radius: 50%; background: var(--mark);
    margin-top: 22px;
  }
  .brand-name {
    margin-top: 10px; text-align: center; color: var(--ink-brand);
    font-family: "Josefin Sans", Arial, sans-serif; font-weight: 400;
    font-size: 30px; letter-spacing: 4px; line-height: 1.1;
  }

  .care {
    position: absolute; left: 481px; top: 26px; width: 57px; height: 211px;
    background: #ffffff; color: var(--ink-dark);
    writing-mode: vertical-lr; padding: 8px 6px;
    font-size: 12.5px; line-height: 1.3;
  }
</style>
</head>
<body>
<main class="sheet">

  <section class="label label--verolinde">
    <div class="details">
      <p class="heading">Verolinde Oil of Anointing</p>
      <p>Contents: Organic oils: Punica granatum, Simmondia chinensis, Limnanthes alba, Rosa, Ravansara aromatica, Chrysopogon zizanoides, Cymbopogon, Pelargonium graveolens. Essences</p>
      <p class="contact">LumenVessel.com.au<br>Tel. +61 400 215 906<br>9 Ashgrove Lane,<br>Merrowdale. NSW, 2150,<br>AUSTRALIA<br>ABN 51 208 377 164</p>
    </div>
    <h2 class="title">Verolinde</h2>
    <p class="subtitle">OIL OF ANOINTING</p>
    <div class="arch"><div class="arch__inner"><span class="brand-dot"></span><p class="brand-name">LUMEN<br>VESSEL</p></div></div>
    <p class="care">Store away from light and heat.<br>External use only.<br>Use by:</p>
  </section>

  <section class="label label--spikenard">
    <div class="details">
      <p class="heading">Spikenard Oil of Anointing</p>
      <p>Contents: Organic Oils, Simmondia chinensis, Nardostachys grandiflora. Essences of Rose, Gold, Chalice Well, Pink Flannel Flower, Helichrysum.</p>
      <p class="contact">LumenVessel.com.au<br>Tel. +61 400 215 906<br>9 Ashgrove Lane,<br>Merrowdale. NSW, 2150,<br>AUSTRALIA<br>ABN 51 208 377 164</p>
    </div>
    <h2 class="title">Spikenard</h2>
    <p class="subtitle">OIL OF ANOINTING</p>
    <div class="arch"><div class="arch__inner"><span class="brand-dot"></span><p class="brand-name">LUMEN<br>VESSEL</p></div></div>
    <p class="care">Store away from light and heat.<br>External use only.<br>Use by:</p>
  </section>

  <section class="label label--amber-hush">
    <div class="details">
      <p class="heading">Spikenard Oil of Anointing</p>
      <p>Contents: Organic Oils, Simmondia chinensis, Nardostachys grandiflora. Essences of Rose, Gold, Chalice Well, Pink Flannel Flower, Helichrysum.</p>
      <p class="contact">LumenVessel.com.au<br>Tel. +61 400 215 906<br>9 Ashgrove Lane,<br>Merrowdale. NSW, 2150,<br>AUSTRALIA<br>ABN 51 208 377 164</p>
    </div>
    <h2 class="title">Amber Hush</h2>
    <p class="subtitle">OIL OF ANOINTING</p>
    <div class="arch"><div class="arch__inner"><span class="brand-dot"></span><p class="brand-name">LUMEN<br>VESSEL</p></div></div>
    <p class="care">Store away from light and heat.<br>External use only.<br>Use by:</p>
  </section>

  <section class="label label--halbrey">
    <div class="details">
      <p class="heading">Spikenard Oil of Anointing</p>
      <p>Contents: Organic Oils, Simmondia chinensis, Nardostachys grandiflora. Essences of Rose, Gold, Chalice Well, Pink Flannel Flower, Helichrysum.</p>
      <p class="contact">LumenVessel.com.au<br>Tel. +61 400 215 906<br>9 Ashgrove Lane,<br>Merrowdale. NSW, 2150,<br>AUSTRALIA<br>ABN 51 208 377 164</p>
    </div>
    <h2 class="title">Halbrey Oil</h2>
    <p class="subtitle">OIL OF ANOINTING</p>
    <div class="arch"><div class="arch__inner"><span class="brand-dot"></span><p class="brand-name">LUMEN<br>VESSEL</p></div></div>
    <p class="care">Store away from light and heat.<br>External use only.<br>Use by:</p>
  </section>

</main>
</body>
</html>
```